Event Space Website (clone)

the name of the company is TOLVAPARTY.com
i’ll have a logo shortly

i basically need a clone of the following website
https://trovehallsnx.com/
i would really like the design to be with stock photos
and then after choosing the winner i will supply my photos
(im doing some all new photo shoots this week)

id love the designer to put their OWN spin on this site

Target Market(s)

nyc urban market

Industry/Entity Type

Event Planning

Coding

Coded - Design and coding required

Number of Pages Required

1 page

Font styles to use
Serif

Requirements
Must have
• from top to bottom ill just list what i need copied

LOCATIONS FAQ CONTACT AND SOCIAL MEDIA LINKS NEED

i need the slider ... for sure

please change classics to current locations
please show
Harlem
Brooklyn
Bronx (for bronx show an image of coming soon)

please change events with a view to
Harlem Venues
1. Tolva Northgate
2. Tolva East Northgate

please change Our biggest and boldest to Brooklyn Venues
1. Tolva Riverbend
2. Tolva Kingsfield (1)
3. Tolva kingsfield (2)
4. Tolva Kingsfield rooftop

remove latest ventures
remove asian couple kissing

keep interested in this location
keep why chose us

keep contact us area
keep social media plug in
Nice to have
• ur own flair and style

PLEASE dont forget that all the individual sections
example
tolva northgate
tolva east northgate
will have their own individual micro pages .... that will be placed under brooklyn venues (ive attached an example for clarity)

```html
<!DOCTYPE html>
<html lang="en">
<head>
<meta charset="utf-8">
<title>Tolva Party</title>
<link rel="stylesheet" href="https://fonts.googleapis.com/css2?family=Source+Serif+4:wght@400;600;700;900&display=swap">
<style>
:root{
  --ink:#1f1f1f;
  --header:#2a2020;
  --footer:#241c1c;
  --accent:#ff5a0a;
  --muted-bg:#f1f1f1;
  --white:#ffffff;
  --label-bg:rgba(12,12,12,.88);
}
*{box-sizing:border-box;margin:0;padding:0}
html,body{width:1200px;height:3508px;overflow:hidden}
body{font-family:'Source Serif 4',serif;color:var(--ink);background:var(--white);position:relative}
.site-header{position:absolute;left:0;top:0;width:1200px;height:127px;background:var(--header);color:var(--white)}
.brand{position:absolute;left:75px;top:40px;font-size:40px;font-weight:900;letter-spacing:.5px;line-height:48px;white-space:nowrap}
.main-nav{position:absolute;top:55px;left:0;font-size:16px;font-weight:700;letter-spacing:.3px}
.main-nav a{position:absolute;color:var(--white);text-decoration:none;white-space:nowrap}
.social{display:flex;gap:22px;position:absolute}
.social span{width:22px;height:22px;border-radius:50%;background:var(--white);display:block}
.site-header .social{left:928px;top:53px}
.hero{position:absolute;left:0;top:127px;width:1200px;height:610px;
  background:radial-gradient(ellipse at 50% 25%,#d89be8 0%,#a43fd0 30%,#7a2aa0 55%,#5a2f4a 80%,#4a3a3a 100%);
  color:var(--white);text-align:center}
.hero-kicker{position:absolute;top:165px;width:100%;font-size:60px;font-weight:900;line-height:64px}
.hero-title{position:absolute;top:222px;width:100%;font-size:94px;font-weight:900;line-height:104px;white-space:nowrap}
.hero-sub{position:absolute;top:322px;width:100%;font-size:33px;font-weight:700}
.btn{background:var(--accent);color:var(--white);font-weight:900;text-transform:uppercase;border:0;font-family:inherit}
.hero .btn{position:absolute;left:505px;top:386px;width:191px;height:51px;font-size:19px}
.dots{position:absolute;top:564px;left:555px;display:flex;gap:14px}
.dots i{width:12px;height:12px;border-radius:50%;background:#111;display:block}
.dots i:first-child{background:var(--white)}
.section-title{position:absolute;width:1200px;text-align:center;font-size:27px;font-weight:700;text-transform:uppercase;letter-spacing:.3px}
.card{position:absolute;overflow:hidden}
.card .photo{position:absolute;inset:0}
.card-label{position:absolute;left:0;bottom:0;height:38px;line-height:38px;padding:0 52px 0 21px;background:var(--label-bg);white-space:nowrap;
  color:var(--white);font-size:17px;font-weight:700;text-transform:uppercase;clip-path:polygon(0 0,calc(100% - 24px) 0,100% 100%,0 100%)}
.card.compact .card-label{font-size:14px;padding:0 34px 0 12px;clip-path:polygon(0 0,calc(100% - 18px) 0,100% 100%,0 100%)}
.coming-soon{position:absolute;left:50%;top:130px;transform:translateX(-50%);border:2px solid var(--white);color:var(--white);
  padding:0 4px;font-size:20px;letter-spacing:4px;line-height:26px;white-space:nowrap}
.steps{position:absolute;left:0;top:2122px;width:1200px;height:395px;background:var(--muted-bg)}
.step,.reason{position:absolute;text-align:center;transform:translateX(-50%)}
.ring{width:78px;height:78px;border:2px solid var(--accent);border-radius:50%;margin:0 auto;display:flex;align-items:center;justify-content:center;background:var(--white)}
.steps .ring{background:transparent}
.ring svg{width:34px;height:34px;fill:var(--accent)}
.step h3,.reason h3{font-size:17px;font-weight:900;text-transform:uppercase;margin-top:16px;white-space:nowrap}
.step p{font-size:17px;line-height:29px;margin-top:2px;white-space:nowrap}
.contact{position:absolute;left:0;top:2856px;width:1200px;height:519px;
  background:linear-gradient(180deg,#141a14 0%,#1f2620 45%,#2b2a2c 75%,#1a1818 100%)}
.contact .section-title{color:var(--white);top:72px}
.field{position:absolute;background:var(--white);font-size:15px;color:#333;padding:0 15px;display:flex;align-items:center}
.field.area{align-items:flex-start;padding-top:18px}
.field .chev{margin-left:auto;width:12px;height:12px}
.contact .btn{position:absolute;left:433px;top:407px;width:334px;height:52px;font-size:19px}
.site-footer{position:absolute;left:0;top:3375px;width:1200px;height:133px;background:var(--footer);color:var(--white);text-align:center}
.site-footer p{position:absolute;top:36px;width:100%;font-size:14px}
.site-footer .social{left:500px;top:70px}
</style>
</head>
<body>

<header class="site-header">
  <div class="brand">TOLVA PARTY</div>
  <nav class="main-nav">
    <a style="left:558px">LOCATIONS</a>
    <a style="left:697px">FAQ</a>
    <a style="left:778px">CONTACT</a>
  </nav>
  <div class="social" aria-label="Social links">
    <span aria-label="Social link 1"></span><span aria-label="Social link 2"></span><span aria-label="Social link 3"></span><span aria-label="Social link 4"></span><span aria-label="Social link 5"></span>
  </div>
</header>

<section class="hero" role="img" aria-label="Banquet hall with round tables and chandeliers lit in purple">
  <div class="hero-kicker">WELCOME TO</div>
  <div class="hero-title">TOLVA PARTY</div>
  <div class="hero-sub">We are an event space company.</div>
  <button class="btn">Read More</button>
  <div class="dots"><i></i><i></i><i></i><i></i></div>
</section>

<h2 class="section-title" style="top:816px">Current Locations</h2>
<div class="card" style="left:75px;top:895px;width:330px;height:283px">
  <div class="photo" role="img" aria-label="Street under an elevated steel viaduct" style="background:linear-gradient(180deg,#6d7280 0%,#3e4046 50%,#2a2b2e 100%)"></div>
  <div class="card-label">Harlem</div>
</div>
<div class="card" style="left:434px;top:895px;width:331px;height:283px">
  <div class="photo" role="img" aria-label="Bridge and skyline at sunset over the river" style="background:linear-gradient(180deg,#5b86a8 0%,#d6a56a 45%,#7e6a52 70%,#3f5666 100%)"></div>
  <div class="card-label">Brooklyn</div>
</div>
<div class="card" style="left:795px;top:895px;width:331px;height:283px;background:#1d1d1d">
  <div class="coming-soon">COMING SOON</div>
  <div class="card-label">Bronx</div>
</div>

<h2 class="section-title" style="top:1249px">Harlem Venues</h2>
<div class="card" style="left:75px;top:1328px;width:512px;height:283px">
  <div class="photo" role="img" aria-label="City towers at night with light trails on a riverside highway" style="background:linear-gradient(180deg,#5a5d8a 0%,#3a3048 40%,#7a5a2a 65%,#2a2530 100%)"></div>
  <div class="card-label">Tolva Northgate</div>
</div>
<div class="card" style="left:614px;top:1328px;width:512px;height:283px">
  <div class="photo" role="img" aria-label="Rooftops of apartment blocks with green trees" style="background:linear-gradient(180deg,#b9bcbf 0%,#9a9590 40%,#6b5a4e 65%,#2f4a2a 100%)"></div>
  <div class="card-label">Tolva East Northgate</div>
</div>

<h2 class="section-title" style="top:1677px">Brooklyn Venues</h2>
<div class="card compact" style="left:75px;top:1756px;width:248px;height:283px">
  <div class="photo" role="img" aria-label="Suspension bridge and skyline at dusk" style="background:linear-gradient(180deg,#3a4a6a 0%,#b07a7a 35%,#3a3040 60%,#15192a 100%)"></div>
  <div class="card-label">Tolva Riverbend</div>
</div>
<div class="card compact" style="left:343px;top:1756px;width:248px;height:283px">
  <div class="photo" role="img" aria-label="Skyline reflected in water under a golden sky" style="background:linear-gradient(180deg,#c9a878 0%,#e0c68a 25%,#3a4a5a 55%,#4a7a9a 80%,#2a5a7a 100%)"></div>
  <div class="card-label">Tolva Kingsfield (1)</div>
</div>
<div class="card compact" style="left:611px;top:1756px;width:248px;height:283px">
  <div class="photo" role="img" aria-label="Waterfront towers in evening light" style="background:linear-gradient(180deg,#7a8fb0 0%,#c9b08a 35%,#4a4e5e 60%,#2e4a62 100%)"></div>
  <div class="card-label">Tolva Kingsfield (2)</div>
</div>
<div class="card compact" style="left:879px;top:1756px;width:248px;height:283px">
  <div class="photo" role="img" aria-label="Rooftop view of city blocks under blue sky" style="background:linear-gradient(180deg,#4a90d0 0%,#8bbbe0 45%,#9a8a78 70%,#5a4538 100%)"></div>
  <div class="card-label">Tolva Kingsfield Rooftop</div>
</div>

<section class="steps">
  <h2 class="section-title" style="top:68px">Interested in this location</h2>
  <div class="step" style="left:196px;top:146px">
    <div class="ring"><svg viewBox="0 0 24 24"><path d="M6 2h8l5 5v15H6z M13 3v5h5" /><rect x="9" y="11" width="7" height="1.6" fill="#fff"/><rect x="9" y="14" width="7" height="1.6" fill="#fff"/><rect x="9" y="17" width="7" height="1.6" fill="#fff"/></svg></div>
    <h3>Send us a note</h3>
    <p>We don't keep you waiting</p>
  </div>
  <div class="step" style="left:467px;top:146px">
    <div class="ring"><svg viewBox="0 0 24 24"><path d="M12 2a7 7 0 0 0-7 7c0 5 7 13 7 13s7-8 7-13a7 7 0 0 0-7-7zm0 9.5A2.5 2.5 0 1 1 12 6.5a2.5 2.5 0 0 1 0 5z"/></svg></div>
    <h3>Check out the location</h3>
    <p>Take a guided tour with<br>a venue rep</p>
  </div>
  <div class="step" style="left:738px;top:146px">
    <div class="ring"><svg viewBox="0 0 24 24"><path d="M3 5h18v17H3z M7 2h2v4H7z M15 2h2v4h-2z"/><g fill="#fff"><rect x="5" y="10" width="3" height="3"/><rect x="10.5" y="10" width="3" height="3"/><rect x="16" y="10" width="3" height="3"/><rect x="5" y="15" width="3" height="3"/><rect x="10.5" y="15" width="3" height="3"/><rect x="16" y="15" width="3" height="3"/></g></svg></div>
    <h3>Pick your perfect date</h3>
    <p>We can help you find the<br>right date</p>
  </div>
  <div class="step" style="left:1005px;top:146px">
    <div class="ring"><svg viewBox="0 0 24 24"><path d="M12 4a8 8 0 0 1 7.4 5H22l-3.5 4-3.5-4h2.2A6 6 0 0 0 6.5 9.5L4.7 8.6A8 8 0 0 1 12 4zM12 20a8 8 0 0 1-7.4-5H2l3.5-4 3.5 4H6.8a6 6 0 0 0 10.7.5l1.8.9A8 8 0 0 1 12 20z"/></svg></div>
    <h3>Plan</h3>
    <p>Check out our vendors<br>have questions?</p>
  </div>
</section>

<h2 class="section-title" style="top:2566px">Why choose us</h2>
<div class="reason" style="left:174px;top:2646px">
  <div class="ring"><svg viewBox="0 0 24 24"><path d="M2 10h4v11H2z M8 10l4-8c2 0 3 1 2.5 3L14 9h6a2 2 0 0 1 2 2.3l-1.4 8A2 2 0 0 1 18.6 21H8z"/></svg></div>
  <h3>Easy</h3>
</div>
<div class="reason" style="left:387px;top:2646px">
  <div class="ring"><svg viewBox="0 0 24 24"><path d="M3 5h18v2H3zM3 11h18v2H3zM3 17h18v2H3z"/><rect x="14" y="3.5" width="2.5" height="5"/><rect x="7" y="9.5" width="2.5" height="5"/><rect x="12" y="15.5" width="2.5" height="5"/></svg></div>
  <h3>Responsive</h3>
</div>
<div class="reason" style="left:599px;top:2646px">
  <div class="ring"><svg viewBox="0 0 24 24"><path d="M16.5 3l4.5 4.5-11 11L5.5 14zM4.5 15l4.5 4.5L3 21z"/></svg></div>
  <h3>Customizable</h3>
</div>
<div class="reason" style="left:812px;top:2646px">
  <div class="ring"><svg viewBox="0 0 24 24"><circle cx="12" cy="8" r="3.2"/><circle cx="5.5" cy="9.5" r="2.5"/><circle cx="18.5" cy="9.5" r="2.5"/><path d="M6.5 19a5.5 5.5 0 0 1 11 0zM1 18a4.5 4.5 0 0 1 6.5-4 7 7 0 0 0-2 4zM23 18a4.5 4.5 0 0 0-6.5-4 7 7 0 0 1 2 4z"/></svg></div>
  <h3>Vendors</h3>
</div>
<div class="reason" style="left:1024px;top:2646px">
  <div class="ring"><svg viewBox="0 0 24 24"><path d="M10 3a7 7 0 0 1 5.6 11.2l5.6 5.6-2 2-5.6-5.6A7 7 0 1 1 10 3zm0 3a4 4 0 1 0 0 8 4 4 0 0 0 0-8z"/></svg></div>
  <h3>Transparent</h3>
</div>

<section class="contact" role="img" aria-label="Outdoor garden venue at night with string lights and trees">
  <h2 class="section-title">Send us a message</h2>
  <div class="field" style="left:253px;top:128px;width:334px;height:52px">Name</div>
  <div class="field" style="left:253px;top:196px;width:334px;height:52px">Email Address</div>
  <div class="field" style="left:253px;top:267px;width:334px;height:52px">Phone No</div>
  <div class="field" style="left:253px;top:334px;width:334px;height:52px">Type of Events</div>
  <div class="field" style="left:616px;top:128px;width:332px;height:52px">Venue of Interest
    <svg class="chev" viewBox="0 0 12 12"><path d="M2 4l4 4 4-4" stroke="#222" stroke-width="2" fill="none"/></svg></div>
  <div class="field area" style="left:616px;top:196px;width:332px;height:190px">Message</div>
  <button class="btn">Submit</button>
</section>

<footer class="site-footer">
  <p>Copyright © 2021. Company Name.All Right Reserved</p>
  <div class="social" aria-label="Social links">
    <span aria-label="Social link 1"></span><span aria-label="Social link 2"></span><span aria-label="Social link 3"></span><span aria-label="Social link 4"></span><span aria-label="Social link 5"></span>
  </div>
</footer>

</body>
</html>
```